Double-sided business card needed - specific brief

We need a double sided business card designed for our company Radiant Trimline. Having lost a lot of weight myself, the back of the card needs to show my before and after pictures. It needs to cover the entire back side of the card. This might be with my two before pictures over set on top of my main after picture or in separate frames. I'll leave that to your artistic consideration. The front needs to have our logo with contact details centred below.

The cards will be printed by PRINTVEX.com and will be rectangular, 84mm x 55mm, but with ROUNDED edges. Please therefore present your designs rectangular but with rounded edges if possible.

The card should be designed in LANDSCAPE orientation.

As well as the logo, the front of the card should have the following details:

Carol Whitby
Weight Loss Motivator with 189lb personal loss
carol@radiant-trimline.example
+44 (0)7700 900418

The website is important so should perhaps be more bold than the rest:
www.radiant-trimline.example

My brand colours are: Pink #CD2366, Light Pink #FD88AD. Blue #1C9CB1, Light Blue #64C4DE

Target Market(s)

Women 30+

Contact Information for Business Card

As description above

Font styles to use
Sans Serif

Requirements
Must have
• Double sided.
• Back side entirely covered with my before and after pictures.
• You may wish to float my before pictures on top of my after picture or add them in different frames. I look forward to seeing your different suggestions.

```html
<!DOCTYPE html>
<html lang="en">
<head>
<meta charset="utf-8">
<title>Radiant Trimline – Business Card</title>
<link rel="stylesheet" href="https://fonts.googleapis.com/css2?family=Lato:wght@300;400;700;900&display=swap">
<style>
  :root{
    --pink:#cd2366;
    --pink-light:#fd88ad;
    --band-pink:#ec7fa6;
    --blue:#1c9cb1;
    --blue-light:#64c4de;
    --paper:#f3f2f0;
    --ink:#2b2b2b;
    --backdrop:#645e7c;
  }
  *{box-sizing:border-box;margin:0;padding:0}
  html,body{width:1200px;height:1200px;overflow:hidden}
  body{background:var(--backdrop);font-family:"Lato",sans-serif;position:relative}

  .card{position:absolute;left:200px;width:800px;height:524px;border-radius:34px;overflow:hidden;
        box-shadow:0 10px 24px rgba(0,0,0,.28)}
  .card--front{top:48px;background:var(--paper)}
  .card--back{top:620px;background:#3a3540}

  /* front */
  .name-band{position:absolute;left:0;top:150px;width:430px;height:150px;background:var(--band-pink);
             padding:26px 0 0 40px;color:#fff}
  .name-band__name{font-size:44px;letter-spacing:1px;line-height:1;text-transform:uppercase}
  .name-band__name b{font-weight:900}
  .name-band__name span{font-weight:300}
  .name-band__rule{width:330px;height:2px;background:#fff;margin:10px 0 10px}
  .name-band__role{font-size:20px;font-weight:400;line-height:1.2}
  .corner-block{position:absolute;right:0;top:46px;width:100px;height:74px;background:var(--band-pink)}
  .brand{position:absolute;left:462px;top:150px;display:flex;align-items:center;gap:12px}
  .brand__dot{width:22px;height:22px;border-radius:50%;background:var(--blue)}
  .brand__name{font-size:34px;font-weight:400;color:var(--pink);letter-spacing:.5px}
  .contacts{position:absolute;left:200px;top:350px;list-style:none}
  .contacts li{display:flex;align-items:center;gap:12px;font-size:23px;color:var(--ink);margin-bottom:8px}
  .contacts li.web{font-weight:900}
  .contacts svg{width:20px;height:20px;flex:none}

  /* back */
  .after-photo{position:absolute;inset:0;
     background:linear-gradient(120deg,#5a5550 0%,#8a7a66 30%,#3f4a68 60%,#2a2f4a 80%,#6a2a30 100%)}
  .before-frame{position:absolute;left:70px;top:150px;width:360px;height:330px;background:#fff;
     transform:rotate(-6deg);padding:22px;box-shadow:0 6px 14px rgba(0,0,0,.35)}
  .before-photo{width:100%;height:100%;background:linear-gradient(160deg,#6d8a55 0%,#a7b78a 40%,#e7e9ee 70%,#5e7a4c 100%)}
  .ribbon{position:absolute;background:var(--blue-light);color:#fff;font-weight:700;font-size:26px;
     letter-spacing:1px;padding:6px 22px}
  .ribbon--before{left:50px;top:220px;transform:rotate(-12deg);background:linear-gradient(90deg,var(--blue-light),var(--blue))}
  .ribbon--after{right:-10px;top:230px;transform:rotate(-12deg);padding:6px 40px 6px 70px;
     background:linear-gradient(90deg,rgba(100,196,222,0),var(--blue) 40%,var(--blue-light))}
  .badge{position:absolute;left:430px;top:290px;width:190px;height:190px;border-radius:50%;background:#fff;
     border:4px dashed var(--blue-light);display:flex;align-items:center;justify-content:center;
     text-align:center;transform:rotate(-12deg)}
  .badge__name{font-size:22px;font-weight:400;color:var(--pink);line-height:1.15}
</style>
</head>
<body>

<section class="card card--front" aria-label="Business card front">
  <div class="corner-block"></div>
  <div class="name-band">
    <h1 class="name-band__name"><b>Carol</b> <span>Whitby</span></h1>
    <div class="name-band__rule"></div>
    <p class="name-band__role">Weight Loss Motivator with<br>189lb personal loss</p>
  </div>
  <div class="brand">
    <span class="brand__dot"></span>
    <span class="brand__name">RADIANT TRIMLINE</span>
  </div>
  <ul class="contacts">
    <li><svg viewBox="0 0 20 20"><path fill="#cd2366" d="M5 2l3 3-2 3c1 2 3 4 5 5l3-2 3 3-2 3C9 18 2 11 2 4z"/></svg>+44 (0)7700 900418</li>
    <li><svg viewBox="0 0 20 20"><rect x="2" y="5" width="16" height="11" fill="#cd2366"/><path d="M2 5l8 6 8-6" stroke="#fff" stroke-width="1.5" fill="none"/></svg>carol@radiant-trimline.example</li>
    <li class="web"><svg viewBox="0 0 20 20"><circle cx="10" cy="10" r="8" fill="#cd2366"/><path d="M2 10h16M10 2v16M4 6h12M4 14h12" stroke="#fff" stroke-width="1"/></svg>www.radiant-trimline.example</li>
  </ul>
</section>

<section class="card card--back" aria-label="Business card back">
  <div class="after-photo" role="img" aria-label="After photo: smiling woman seated on a sofa in a living room"></div>
  <div class="before-frame">
    <div class="before-photo" role="img" aria-label="Before photo: woman in a white shirt holding a dog in a garden"></div>
  </div>
  <div class="ribbon ribbon--before">BEFORE</div>
  <div class="ribbon ribbon--after">AFTER</div>
  <div class="badge"><span class="badge__name">RADIANT<br>TRIMLINE</span></div>
</section>

</body>
</html>
```